CoralPeak Holdings Inc. Business Card Design

My business is custom renovations and homes.I would need to have a new business logo created to go along with my company name. The business card should be of a modern style as this is the market I am focused on. I would need my contact information and website posted on the card. I would also like to list a few of the tasks I conduct on the card (such as: Renovations, Additions, Repairs, New Homes, Design, Consultations). On the reverse of the card I currently have just my logo and my motto, "Crafting A Bold Dawn". However, I am open to completely changing everything as I am starting a new year and would like to excel further. Any new ideas and suggestions are always welcomed. Thank you.

Target Market(s)

Upscale residential and commercial renovations and builds

Industry/Entity Type

Business

Contact Information for Business Card

I would like the design to be able to be laser cut or burnt onto a wooden business card. I will be creating one option of cards for really loyal customers (wooden) and a second option for the everyday customer (paper).

Font styles to use
Other font styles liked:
• Calibri / anything of mordern taste

Colors
f37122
5c5c5c
474747
ffffff

Requirements
Must have
• I would like the colours of my business to be a sharp orange and grey. I believe this will symbolize a modern style. I am open to other suggestions if this is not suitable for the designers tastes. My contact info as follows:
• Jack Merlin
• President
• CoralPeak Holdings Inc.
• 555-392-7184
• jack@coralpeakholdings.example
• I would like my website (currently under construction) coralpeakholdings.example on the card aswell.
Nice to have
• Along with a modern logo representing CoralPeak, I would like something on the card besides the logo and contact information. Perhaps a small background design. I feel it may be nice to have my services listed on the card (in smaller font on the bottom) Renovations, Additions, Repairs, Design, Consultations.
Should not have
• The business card should not have too many different colors. Should not have rounded corners.

```html
<!DOCTYPE html>
<html lang="en">
<head>
<meta charset="utf-8">
<title>CoralPeak Holdings Inc. — Business Card</title>
<link rel="stylesheet" href="https://fonts.googleapis.com/css2?family=Michroma&family=Source+Sans+3:wght@400;600&display=swap">
<style>
  :root {
    --orange: #f37122;
    --orange-deep: #d9600f;
    --grey: #5c5c5c;
    --grey-dark: #474747;
    --ink: #2b2b2b;
    --white: #ffffff;
    --paper: #f2f2f1;
    --backdrop: #3b3432;
    --heading: "Michroma", sans-serif;
    --body: "Source Sans 3", sans-serif;
  }
  * { box-sizing: border-box; margin: 0; padding: 0; }
  html, body { width: 1200px; height: 844px; overflow: hidden; }
  body {
    background: var(--backdrop);
    display: flex;
    align-items: center;
    justify-content: center;
    gap: 60px;
    font-family: var(--body);
  }
  .card {
    width: 520px;
    height: 300px;
    position: relative;
    box-shadow: 0 10px 30px rgba(0,0,0,.45);
  }

  /* Front: contact side */
  .card-front {
    background: var(--paper);
    color: var(--grey-dark);
    text-align: center;
    padding-top: 40px;
  }
  .brand-name {
    font-family: var(--heading);
    font-size: 30px;
    letter-spacing: 1px;
    color: var(--ink);
    line-height: 1;
  }
  .brand-sub {
    display: flex;
    align-items: center;
    justify-content: center;
    gap: 12px;
    margin-top: 6px;
    font-family: var(--heading);
    font-size: 13px;
    letter-spacing: 1px;
    color: var(--grey);
  }
  .brand-sub::before, .brand-sub::after {
    content: "";
    width: 70px;
    height: 1px;
    background: #b5b5b5;
  }
  .person-name {
    margin-top: 14px;
    font-family: var(--heading);
    font-size: 14px;
    letter-spacing: 1px;
    color: var(--ink);
  }
  .person-name .surname { color: var(--orange); }
  .person-title { font-size: 12px; color: var(--grey-dark); margin-top: 1px; }
  .contact { margin-top: 12px; font-size: 13px; line-height: 1.35; color: var(--ink); }
  .contact .label { color: var(--orange); font-weight: 600; }
  .contact .website { color: var(--orange); }
  .services {
    position: absolute;
    left: 0; right: 0; bottom: 20px;
    font-size: 14px;
    color: var(--ink);
    letter-spacing: .2px;
  }

  /* Back: brand side */
  .card-back {
    background: var(--orange-deep);
    color: var(--white);
  }
  .back-rule {
    position: absolute;
    left: 0; right: 0;
    top: 232px;
    height: 1px;
    background: rgba(255,255,255,.7);
  }
  .back-brand {
    position: absolute;
    left: 0; right: 0;
    top: 88px;
    text-align: center;
  }
  .back-mark {
    display: block;
    margin: 0 auto 12px;
    width: 28px;
    height: 28px;
  }
  .back-name {
    font-family: var(--heading);
    font-size: 26px;
    letter-spacing: 1px;
    line-height: 1;
  }
  .back-sub {
    display: flex;
    align-items: center;
    justify-content: center;
    gap: 10px;
    margin-top: 5px;
    font-family: var(--heading);
    font-size: 11px;
    letter-spacing: 1px;
  }
  .back-sub::before, .back-sub::after,
  .motto::before, .motto::after {
    content: "";
    width: 50px;
    height: 1px;
    background: var(--white);
  }
  .motto {
    display: flex;
    align-items: center;
    justify-content: center;
    gap: 10px;
    margin-top: 8px;
    font-size: 14px;
    letter-spacing: 2px;
    text-transform: uppercase;
  }
</style>
</head>
<body>
  <section class="card card-front">
    <div class="brand-name">CoralPeak</div>
    <div class="brand-sub">HOLDINGS INC.</div>
    <div class="person-name">JACK <span class="surname">MERLIN</span></div>
    <div class="person-title">President</div>
    <div class="contact">
      <div><span class="label">P:</span> 555-392-7184</div>
      <div><span class="label">E:</span> jack@coralpeakholdings.example</div>
      <div class="website">www.coralpeakholdings.example</div>
    </div>
    <div class="services">Renovations | Additions | Repairs | New Homes | Design | Consultations</div>
  </section>

  <section class="card card-back">
    <div class="back-brand">
      <svg class="back-mark" viewBox="0 0 28 28" aria-hidden="true">
        <circle cx="14" cy="14" r="12" fill="none" stroke="#ffffff" stroke-width="3"/>
      </svg>
      <div class="back-name">CoralPeak</div>
      <div class="back-sub">HOLDINGS INC.</div>
      <div class="motto">Crafting A Bold Dawn</div>
    </div>
    <div class="back-rule"></div>
  </section>
</body>
</html>
```